Physician focused educational website needed

We are looking to create a fresh, simple website to help Physicians understand the benefits of protecting their largest asset....their income. We are wanting to create a site that can be a resource to help answer the FAQ that physicians ask regarding Disability Insurance. The goal is not to sell DI but rather to education the physician on the importance of the product and to be a resource for them to learn more.

Target Market(s)

Physicians

Industry/Entity Type

Insurance

Coding

Coded - Design and coding required

Number of Pages Required

1 page

Requirements
Must have
• easy to navigate and understand FAQ format

```html
<!DOCTYPE html>
<html lang="en">
<head>
<meta charset="utf-8">
<title>MedIncome Guard – Disability Insurance for Physicians</title>
<link href="https://fonts.googleapis.com/css2?family=Montserrat:wght@400;500;600;700&family=Open+Sans:wght@400;600&display=swap" rel="stylesheet">
<style>
:root{
  --blue:#159ad9;
  --blue-dark:#0f7fb8;
  --green:#0a9a0a;
  --green-dark:#087a08;
  --orange:#e57c0a;
  --ink:#222;
  --muted:#555;
  --bar:#e9e9e9;
  --bar-line:#d4d4d4;
  --footer:#ececec;
  --white:#fff;
}
*{box-sizing:border-box;margin:0;padding:0}
html,body{width:1200px;height:2486px;overflow:hidden;background:var(--white)}
body{font-family:"Open Sans",sans-serif;color:var(--ink);position:relative}
a{color:inherit;text-decoration:none}

/* header */
.site-header{position:absolute;left:0;top:0;width:1200px;height:108px;border-top:4px solid var(--blue);background:var(--white)}
.brand{position:absolute;left:99px;top:30px;display:flex;align-items:center;gap:12px;font-family:"Montserrat",sans-serif;font-weight:700;font-size:24px;color:var(--blue)}
.brand-mark{width:34px;height:34px;background:var(--green)}
.main-nav a{position:absolute;top:43px;height:37px;display:flex;align-items:center;justify-content:center;font-family:"Montserrat",sans-serif;font-weight:500;font-size:15.5px;color:var(--ink);white-space:nowrap}
.main-nav a.active{border:2px solid var(--blue);color:var(--blue)}
.nav-home{left:457px;width:74px}
.nav-about{left:572px}
.nav-faq{left:678px}
.nav-contact{left:769px}
.cta{position:absolute;left:873px;top:36px;width:228px;height:50px;background:var(--blue);color:var(--white);font-family:"Montserrat",sans-serif;font-weight:600;font-size:14.5px;display:flex;align-items:center;justify-content:center;white-space:nowrap}

/* hero */
.hero{position:absolute;left:0;top:108px;width:1200px;height:515px;background:linear-gradient(90deg,#8f9499 0%,#b8bcc0 40%,#d9dcdf 100%)}
.hero-photo{position:absolute;left:440px;top:0;width:760px;height:515px;background:linear-gradient(180deg,#e6e9ec 0%,#cdd8d6 55%,#b9c6c4 100%)}
.hero-title{position:absolute;left:96px;top:103px;font-family:"Montserrat",sans-serif;font-weight:600;font-size:41px;color:var(--white);letter-spacing:.3px;white-space:nowrap}
.hero-text{position:absolute;left:99px;top:185px;width:490px;font-weight:600;font-size:16.5px;line-height:33px;color:var(--white)}
.hero-btn{position:absolute;left:99px;top:288px;width:139px;height:53px;background:var(--blue-dark);border:2px solid var(--white);color:var(--white);font-family:"Montserrat",sans-serif;font-weight:500;font-size:16.5px;display:flex;align-items:center;justify-content:center}
.hero-dots{position:absolute;left:99px;top:396px;display:flex;gap:5px}
.hero-dots span{width:16px;height:16px;border-radius:50%;border:2px solid var(--white)}
.hero-dots span.on{background:var(--blue)}

/* intro */
.intro-title{position:absolute;left:0;top:678px;width:1200px;text-align:center;font-family:"Montserrat",sans-serif;font-weight:500;font-size:30px;color:var(--blue)}
.intro-text{position:absolute;left:0;top:730px;width:1200px;text-align:center;font-size:14.5px;color:#444}

/* topic cards */
.topics{position:absolute;left:99px;top:853px;width:1002px;height:278px;display:flex}
.topic{position:relative;flex:1;height:278px;background:var(--green);border:3px solid var(--green-dark);box-shadow:inset 0 0 0 3px rgba(255,255,255,.5);color:var(--white);text-align:center}
.topic.featured{background:var(--orange);border-color:#c96a06}
.topic.featured::after{content:"";position:absolute;left:50%;bottom:-25px;margin-left:-20px;border:20px solid transparent;border-top-color:var(--orange);border-bottom:0;height:0}
.topic-icon{position:absolute;left:50%;top:-63px;margin-left:-60px;width:120px;height:120px;border-radius:50%;background:var(--green);border:5px solid var(--white);display:flex;align-items:center;justify-content:center}
.topic.featured .topic-icon{background:var(--orange)}
.topic-title{position:absolute;left:20px;right:20px;top:108px;font-weight:600;font-size:16.5px;line-height:33px;text-transform:uppercase}
.topic-btn{position:absolute;left:50%;top:199px;margin-left:-59px;width:118px;height:38px;border:2px solid var(--white);border-radius:19px;font-weight:600;font-size:12.5px;display:flex;align-items:center;justify-content:center}

/* faq */
.faq-title{position:absolute;left:99px;top:1196px;font-family:"Montserrat",sans-serif;font-weight:600;font-size:24px;color:var(--blue)}
.faq-item{position:absolute;left:99px;width:1002px;height:53px;background:var(--bar);border:1px solid var(--bar-line);font-size:15px;color:#333;display:flex;align-items:center;padding-left:14px}
.faq-toggle{position:absolute;right:3px;top:3px;width:46px;height:45px;background:var(--blue);display:flex;align-items:center;justify-content:center}
.faq-answer{position:absolute;left:99px;top:1341px;width:1002px;height:147px}
.faq-photo{position:absolute;left:0;top:0;width:163px;height:147px;border:1px solid #ccc;background:linear-gradient(135deg,#f2f2f2 0%,#d8dcdf 50%,#9aa2a8 100%)}
.faq-body{position:absolute;left:188px;top:0;width:814px;font-size:12.3px;line-height:25px;color:#333}
.faq-body p+p{margin-top:8px}

/* footer */
.site-footer{position:absolute;left:0;top:2094px;width:1200px;height:392px;background:var(--footer);border-top:4px solid var(--blue)}
.footer-title{position:absolute;left:0;top:32px;width:1200px;text-align:center;font-family:"Montserrat",sans-serif;font-weight:500;font-size:22px;color:#222}
.footer-text{position:absolute;left:200px;top:80px;width:800px;text-align:center;font-size:13.5px;line-height:25px;color:#444}
.contact-row{position:absolute;left:318px;top:163px;display:flex;gap:26px;font-family:"Montserrat",sans-serif;font-size:19px;color:#222}
.contact-row span{display:flex;align-items:center;gap:14px}
.contact-icon{width:44px;height:44px;border-radius:50%;border:2px solid var(--blue);display:flex;align-items:center;justify-content:center}
.footer-nav{position:absolute;left:0;top:261px;width:1200px;display:flex;justify-content:center;font-family:"Montserrat",sans-serif;font-weight:500;font-size:16px;color:#222}
.footer-nav a+a::before{content:"|";margin:0 18px;color:#222}
.footer-rule{position:absolute;left:99px;top:316px;width:1002px;height:1px;background:#bbb}
.copyright{position:absolute;left:99px;top:344px;font-family:"Montserrat",sans-serif;font-weight:500;font-size:14px;color:#222}
.social{position:absolute;left:873px;top:333px;display:flex;gap:10px}
.social span{width:37px;height:37px;border-radius:50%;border:2px solid #222}
</style>
</head>
<body>

<header class="site-header">
  <a class="brand" href="#"><span class="brand-mark"></span>MedIncome Guard</a>
  <nav class="main-nav">
    <a class="nav-home active" href="#">Home</a>
    <a class="nav-about" href="#">About</a>
    <a class="nav-faq" href="#">FAQ</a>
    <a class="nav-contact" href="#">Contact Us</a>
  </nav>
  <a class="cta" href="#">NEED MORE INFORMATION</a>
</header>

<section class="hero">
  <div class="hero-photo" role="img" aria-label="Group of smiling physicians and nurses in white coats and scrubs in a bright hospital corridor"></div>
  <h1 class="hero-title">DISABILITY INSURANCE</h1>
  <p class="hero-text">We help Physicians understand the benefits of protecting<br>their largest asset....their income.</p>
  <a class="hero-btn" href="#">READ MORE</a>
  <div class="hero-dots"><span class="on"></span><span></span><span></span><span></span><span></span></div>
</section>

<h2 class="intro-title">Income Protection Insurance</h2>
<p class="intro-text">Excepteur sint occaecat cupidatat non proident, sunt in culpa qui officia deserunt.</p>

<section class="topics">
  <article class="topic">
    <div class="topic-icon">
      <svg width="60" height="60" viewBox="0 0 60 60" fill="none" stroke="#fff" stroke-width="3"><circle cx="32" cy="18" r="13" fill="#fff"/><text x="32" y="25" text-anchor="middle" font-family="Open Sans,sans-serif" font-weight="700" font-size="19" fill="#0a9a0a" stroke="none">$</text><path d="M6 44h10l10 4h14l10-8" stroke-linecap="round" stroke-linejoin="round"/><path d="M6 52h12l10 3h14l12-10"/></svg>
    </div>
    <h3 class="topic-title">Why do I need to buy private income protection/DI</h3>
    <a class="topic-btn" href="#">READ MORE</a>
  </article>
  <article class="topic featured">
    <div class="topic-icon">
      <svg width="62" height="62" viewBox="0 0 62 62" fill="none" stroke="#fff" stroke-width="3.5"><path d="M22 8a14 12 0 1 0-8 22l-4 6 9-4"/><circle cx="38" cy="34" r="17"/><path d="M33 29a5 5 0 1 1 6 5v4" stroke-linecap="round"/><circle cx="39" cy="44" r="1.5" fill="#fff"/></svg>
    </div>
    <h3 class="topic-title">As a physician, what should I look for in DI coverage</h3>
    <a class="topic-btn" href="#">READ MORE</a>
  </article>
  <article class="topic">
    <div class="topic-icon">
      <svg width="60" height="60" viewBox="0 0 60 60" fill="none" stroke="#fff" stroke-width="3"><rect x="14" y="10" width="34" height="44" rx="3"/><rect x="24" y="6" width="14" height="8" rx="2"/><path d="M28 24h14M28 32h14M28 40h14" stroke-linecap="round"/><path d="M8 26l8-3 8 3v6c0 6-8 10-8 10s-8-4-8-10z" fill="#0a9a0a"/><path d="M16 28v8M12 32h8"/></svg>
    </div>
    <h3 class="topic-title">When should I purchase coverage?</h3>
    <a class="topic-btn" href="#">READ MORE</a>
  </article>
</section>

<h2 class="faq-title">Frequently Asked Questions?</h2>

<div class="faq-item" style="top:1261px">When is the right time to buy Income Protection plan/should I buy while in training/Is there an advantage to buying as a PGY 1?<span class="faq-toggle"><svg width="16" height="16"><path d="M2 8h12" stroke="#fff" stroke-width="3"/></svg></span></div>

<div class="faq-answer">
  <div class="faq-photo" role="img" aria-label="Close-up of hands signing an insurance document with a pen"></div>
  <div class="faq-body">
    <p>The right time to buy insurance is today.  Our health can change in an instant so buying coverage while you are young and healthy is imperative.  Even as a PGY1, locking in your insurability is important.  As more and more residents are starting to take medications for stress and anxiety during these difficult years, your ability to get insurance can be drastically impacted.</p>
    <p>What matters is that you obtain some form of coverage with the ability to purchase more later regardless of your health.  At the very latest, you should make sure you are securing coverage before leaving your training program because you receive significant discounts while in training that you won't be able to get once you leave.</p>
  </div>
</div>

<div class="faq-item" style="top:1514px">Wouldn't my group coverage cover me adequately? (what is the difference between group/private)<span class="faq-toggle"><svg width="16" height="16"><path d="M2 8h12M8 2v12" stroke="#fff" stroke-width="3"/></svg></span></div>
<div class="faq-item" style="top:1583px">What features should I look for?<span class="faq-toggle"><svg width="16" height="16"><path d="M2 8h12M8 2v12" stroke="#fff" stroke-width="3"/></svg></span></div>
<div class="faq-item" style="top:1652px">What is true own occupation/specialty specific mean?<span class="faq-toggle"><svg width="16" height="16"><path d="M2 8h12M8 2v12" stroke="#fff" stroke-width="3"/></svg></span></div>
<div class="faq-item" style="top:1720px">What is Catestrophic Benefit?<span class="faq-toggle"><svg width="16" height="16"><path d="M2 8h12M8 2v12" stroke="#fff" stroke-width="3"/></svg></span></div>
<div class="faq-item" style="top:1789px">What is DIRS? (disability income retirement supplement)<span class="faq-toggle"><svg width="16" height="16"><path d="M2 8h12M8 2v12" stroke="#fff" stroke-width="3"/></svg></span></div>
<div class="faq-item" style="top:1858px">What if my health changes after I buy coverage?<span class="faq-toggle"><svg width="16" height="16"><path d="M2 8h12M8 2v12" stroke="#fff" stroke-width="3"/></svg></span></div>
<div class="faq-item" style="top:1927px">Can I raise my coverage after I enter practice?<span class="faq-toggle"><svg width="16" height="16"><path d="M2 8h12M8 2v12" stroke="#fff" stroke-width="3"/></svg></span></div>
<div class="faq-item" style="top:1995px">What is inflation protection? (COLA)<span class="faq-toggle"><svg width="16" height="16"><path d="M2 8h12M8 2v12" stroke="#fff" stroke-width="3"/></svg></span></div>

<footer class="site-footer">
  <h2 class="footer-title">Got a question or comment?</h2>
  <p class="footer-text">We are constantly working to raise the bar on our services. If you have any questions or concerns about your experience, please let us know.</p>
  <div class="contact-row">
    <span><span class="contact-icon"><svg width="20" height="20" viewBox="0 0 20 20"><path d="M5 2l3 4-2 2c1 3 3 5 6 6l2-2 4 3-2 3C9 18 2 11 2 4z" fill="none" stroke="#159ad9" stroke-width="1.8" stroke-linejoin="round"/></svg></span>Call: 180 555 0142</span>
    <span><span class="contact-icon"><svg width="20" height="16" viewBox="0 0 20 16"><rect x="1" y="1" width="18" height="14" rx="2" fill="#159ad9"/><path d="M2 3l8 6 8-6" fill="none" stroke="#fff" stroke-width="1.6"/></svg></span>Mail: info@medincomeguard.com</span>
  </div>
  <nav class="footer-nav">
    <a href="#">Home</a><a href="#">About Us</a><a href="#">FAQ</a><a href="#">Privacy</a><a href="#">Terms of Use</a><a href="#">Contact Us</a><a href="#">Sitemap</a>
  </nav>
  <div class="footer-rule"></div>
  <p class="copyright">Copyright © 2016 MedIncome Guard. All Right Reserved</p>
  <div class="social"><span></span><span></span><span></span><span></span><span></span></div>
</footer>

</body>
</html>
```